Business cards for a tribute and obituary website

Our website is called Quiet Orchard.

It is a special place online for people to remember their loved ones who have passed away, through obituaries and tributes. Friends and family can also convey their condolences on the deceased's memorial page. Celebrating the life of the deceased and remembering their legacy is very important to us – death should not be just about grieving.

We would like the card to look tasteful and modern. The design should ideally not have colours that are too bright. The logo and website URL, www.quietorchardpages.net should be visible on the front of the card, with our slogan "Honouring a story well told" on the back.

The design should communicate our purpose – remembering loved ones who have passed – and also a lighter tone of celebrating life. It should not look like a funeral director's card!

Our logo has been attached. Looking forward to some beautiful designs! Get creative :)
Updates

Reason: Thank you all for your designs. The rest of my team and I have not reached a decision on which design to select and I am collecting feedback from them. I will provide feedback for any changes that need to be made soon. It would be great if we could see more original designs and in more colours! We will definitely select a design by this deadline.

Industry/Entity Type

Business

Contact Information for Business Card

Nadia Fenwick
Project Manager
471226809
nadiafenwick@quietorchardpages.net

Font styles to use
Serif
Sans Serif

Requirements
Must have
• Logo and website address (www.quietorchardpages.net) on the front.
Nice to have
• Hi designers! It would be nice to see alternative colours – feel free to try out colours that are tasteful and subtle. The colour of the business card does not have to be the same as the logo.
• We would also like to see the logo used in different ways, perhaps a glossy or embossed finish. The card should look stylish.

```html
<!DOCTYPE html>
<html lang="en">
<head>
<meta charset="utf-8">
<title>Quiet Orchard – Business Cards</title>
<link rel="stylesheet" href="https://fonts.googleapis.com/css2?family=Bitter:wght@700&family=PT+Serif:wght@400;700&display=swap">
<style>
  :root {
    --backdrop: #e8e5e0;
    --paper: #ffffff;
    --navy: #1d4a72;
    --navy-deep: #0d2f52;
    --navy-light: #3e6e96;
    --ink: #2a3f57;
    --muted: #5a6b7c;
    --faint: #ececec;
  }
  * { margin: 0; padding: 0; box-sizing: border-box; }
  html, body {
    width: 1200px; height: 1023px; overflow: hidden;
    background: var(--backdrop);
  }
  .card {
    position: absolute;
    width: 560px; height: 320px;
    border-radius: 4px;
    box-shadow: 0 12px 30px rgba(0,0,0,.18);
    overflow: hidden;
  }
  .card-front { left: 80px; top: 110px; background: var(--paper); }
  .card-back {
    left: 560px; top: 590px;
    background: radial-gradient(ellipse at 30% 80%, var(--navy-light) 0%, var(--navy) 45%, var(--navy-deep) 100%);
  }

  .faint-mark {
    position: absolute; right: -40px; top: -60px;
    width: 220px; height: 220px; border-radius: 50%;
    background: var(--faint);
  }

  .brand { display: flex; align-items: center; gap: 16px; }
  .brand-dot { width: 58px; height: 58px; border-radius: 50%; flex: none; }
  .brand-name {
    font-family: "Bitter", Georgia, serif; font-weight: 700;
    line-height: .95; font-size: 44px;
  }
  .card-front .brand { position: absolute; left: 40px; top: 48px; }
  .card-front .brand-dot { background: var(--navy); }
  .card-front .brand-name { color: var(--navy); }

  .contact { position: absolute; left: 40px; top: 176px; font-family: "PT Serif", Georgia, serif; }
  .person { display: flex; align-items: baseline; gap: 10px; margin-bottom: 12px; }
  .person-name { font-weight: 700; font-size: 19px; color: var(--navy); }
  .divider { width: 1px; height: 18px; background: var(--muted); align-self: center; }
  .person-role { font-size: 14px; color: var(--muted); }
  .contact-list { list-style: none; }
  .contact-list li {
    display: flex; align-items: center; gap: 9px;
    font-size: 14px; color: var(--ink); margin-bottom: 4px;
  }
  .contact-icon { width: 13px; height: 13px; flex: none; }

  .card-back .brand { position: absolute; left: 150px; top: 92px; gap: 26px; }
  .card-back .brand-dot { background: var(--paper); width: 96px; height: 96px; }
  .card-back .brand-name { color: var(--paper); font-size: 40px; }
  .slogan {
    position: absolute; left: 150px; top: 200px;
    font-family: "Bitter", Georgia, serif; font-weight: 700;
    font-size: 16px; color: var(--paper); letter-spacing: .3px;
  }
</style>
</head>
<body>

<section class="card card-front" aria-label="Card front">
  <div class="faint-mark" aria-hidden="true"></div>
  <div class="brand">
    <span class="brand-dot" aria-hidden="true"></span>
    <h1 class="brand-name">Quiet<br>Orchard</h1>
  </div>
  <div class="contact">
    <p class="person">
      <span class="person-name">Nadia Fenwick</span>
      <span class="divider" aria-hidden="true"></span>
      <span class="person-role">Project Manager</span>
    </p>
    <ul class="contact-list">
      <li>
        <svg class="contact-icon" viewBox="0 0 13 13" aria-hidden="true"><rect width="13" height="13" rx="2" fill="#1d4a72"/><path d="M4 3.2c.5-.3.9 0 1.1.5l.4 1c.1.3 0 .6-.3.8l-.4.3c.4.9 1.1 1.6 2 2l.3-.4c.2-.3.5-.4.8-.3l1 .4c.5.2.8.6.5 1.1-.4.7-1.1 1-1.9.7C5.6 8.6 4.3 7.3 3.6 5.5c-.3-.8 0-1.6.4-2.3z" fill="#fff"/></svg>
        <span>471 226 809</span>
      </li>
      <li>
        <svg class="contact-icon" viewBox="0 0 13 13" aria-hidden="true"><rect width="13" height="13" rx="2" fill="#1d4a72"/><rect x="2.5" y="3.8" width="8" height="5.6" fill="none" stroke="#fff" stroke-width="1"/><path d="M2.5 3.8l4 3 4-3" fill="none" stroke="#fff" stroke-width="1"/></svg>
        <span>nadiafenwick@quietorchardpages.net</span>
      </li>
      <li>
        <svg class="contact-icon" viewBox="0 0 13 13" aria-hidden="true"><rect width="13" height="13" rx="2" fill="#1d4a72"/><circle cx="6.5" cy="6.5" r="3.8" fill="none" stroke="#fff" stroke-width="1"/><ellipse cx="6.5" cy="6.5" rx="1.6" ry="3.8" fill="none" stroke="#fff" stroke-width=".8"/><path d="M2.7 6.5h7.6" stroke="#fff" stroke-width=".8"/></svg>
        <span>www.quietorchardpages.net</span>
      </li>
    </ul>
  </div>
</section>

<section class="card card-back" aria-label="Card back">
  <div class="brand">
    <h2 class="brand-name">Quiet<br>Orchard</h2>
    <span class="brand-dot" aria-hidden="true"></span>
  </div>
  <p class="slogan">Honouring a story well told</p>
</section>

</body>
</html>
```